Electrician Needs A Business Card

I already have a logo and would like a business card to be designed based around this logo the company is called Coralwood Electrical Pty Ltd

The business card will be printed on transparent plastic so I need it to stand out from the crowd. I do not want the card to have anything to do with Electrical on it eg light bulbs, power points etc

I need it to have the following details.

Dominic Farrow
Mobile : 0452 317 908
email : dominic@coralwoodelectrical.com.au

If it could incorporate the following onto the bottom of the card
ELECTRICAL - COMMUNICATIONS - AUDIO - VISUAL

```html
<!DOCTYPE html>
<html lang="en">
<head>
<meta charset="utf-8">
<title>Coralwood Electrical – Business Card</title>
<link rel="stylesheet" href="https://fonts.googleapis.com/css2?family=Jost:wght@400;500;600;700&display=swap">
<style>
  :root {
    --amber: #f5a623;
    --ink: #141414;
    --stage: #ececec;
    --clear-card: #d9d9d9;
    --tint-card: #d8b48a;
    --rule: #1e1e1e;
    --white: #ffffff;
  }
  * { box-sizing: border-box; margin: 0; padding: 0; }
  html, body { width: 960px; height: 1200px; overflow: hidden; }
  body {
    background: var(--stage);
    font-family: "Jost", "Futura", sans-serif;
    color: var(--ink);
    position: relative;
  }
  .card {
    position: absolute;
    left: 160px;
    width: 640px;
    height: 390px;
    border-radius: 18px;
    overflow: hidden;
    box-shadow: 0 10px 30px rgba(0,0,0,.18);
  }
  .card--clear { top: 60px; background: var(--clear-card); }
  .card--tinted { top: 760px; background: var(--tint-card); }

  .card__pattern {
    position: absolute;
    left: 20px; top: 26px;
    width: 160px; height: 62px;
    background: linear-gradient(90deg, var(--amber) 0%, var(--ink) 50%, var(--amber) 100%);
    opacity: .85;
  }
  .card__company {
    position: absolute;
    right: 30px; top: 40px;
    font-weight: 500;
    font-size: 30px;
    line-height: 1.1;
    letter-spacing: .5px;
    text-transform: uppercase;
    white-space: nowrap;
  }
  .card__rule {
    position: absolute;
    left: 0; right: 0; top: 104px;
    height: 3px;
    background: var(--rule);
  }
  .card__mark {
    position: absolute;
    right: 48px; top: 128px;
    width: 180px; height: 180px;
    background: var(--amber);
  }
  .card__person {
    position: absolute;
    left: 36px; top: 196px;
  }
  .card__name {
    font-weight: 700;
    font-size: 30px;
    line-height: 1.1;
    margin-bottom: 8px;
  }
  .card__contact {
    font-weight: 500;
    font-size: 14px;
    line-height: 1.3;
  }
  .card__band {
    position: absolute;
    left: 0; right: 0; bottom: 0;
    height: 62px;
    background: var(--ink);
    color: var(--amber);
    display: flex;
    align-items: center;
    justify-content: center;
    font-weight: 600;
    font-size: 19px;
    letter-spacing: .5px;
    white-space: nowrap;
  }

  .lockup {
    position: absolute;
    top: 560px; left: 0; right: 0;
    display: flex;
    align-items: center;
    justify-content: center;
    gap: 18px;
  }
  .lockup__square {
    width: 80px; height: 80px;
    background: var(--amber);
  }
  .lockup__name {
    font-weight: 500;
    font-size: 30px;
    text-transform: uppercase;
    letter-spacing: .5px;
  }
</style>
</head>
<body>

  <section class="card card--clear">
    <div class="card__pattern" role="img" aria-label="Decorative band of amber and black triangles"></div>
    <div class="card__company">Coralwood Electrical</div>
    <div class="card__rule"></div>
    <div class="card__mark"></div>
    <div class="card__person">
      <p class="card__name">Dominic Farrow</p>
      <p class="card__contact">Mobile : 0452 317 908</p>
      <p class="card__contact">email : dominic@coralwoodelectrical.com.au</p>
    </div>
    <div class="card__band">ELECTRICAL - COMMUNICATIONS - AUDIO - VISUAL</div>
  </section>

  <div class="lockup">
    <div class="lockup__square"></div>
    <div class="lockup__name">Coralwood Electrical</div>
  </div>

  <section class="card card--tinted">
    <div class="card__pattern" role="img" aria-label="Decorative band of amber and black triangles"></div>
    <div class="card__company">Coralwood Electrical</div>
    <div class="card__rule"></div>
    <div class="card__mark"></div>
    <div class="card__person">
      <p class="card__name">Dominic Farrow</p>
      <p class="card__contact">Mobile : 0452 317 908</p>
      <p class="card__contact">email : dominic@coralwoodelectrical.com.au</p>
    </div>
    <div class="card__band">ELECTRICAL - COMMUNICATIONS - AUDIO - VISUAL</div>
  </section>

</body>
</html>
```